New Company Business Card Design

I have a new company logo and I want a new business card design. I dont know if the logo file i attached is in the correct format or quality. We are a New York City Specialty construction Firm specializing in high risk out of the box projects. I want a simple and classy business card that people will his card is as crisp as the work his company does.

Target Market(s)

Clients in the heavy construction industry in New York City

Industry/Entity Type

Construction Company

Contact Information for Business Card

Simple Classy - DIFFERENT

Font styles to use
Other font styles liked:
• Mach the logo font in some way

Colors

Designer to choose colors to be used in the design.

Requirements
Must have
• Uniqueness
Nice to have
• Nothing particular - Just different and classy - Timeless
Should not have
• Goofy Shit or Gimmicky shit

```html
<!DOCTYPE html>
<html lang="en">
<head>
<meta charset="utf-8">
<title>Kestrel Row Builders – Business Cards</title>
<link href="https://fonts.googleapis.com/css2?family=Source+Sans+3:wght@400;700&display=swap" rel="stylesheet">
<style>
  :root {
    --backdrop: #2f2a28;
    --card: #121212;
    --card-edge: #1c1c1c;
    --ink: #f2f2f2;
    --muted: #8a8a8a;
    --silver: #9c9c9c;
    --accent: #1f6fc6;
    --divider: #5a5a5a;
  }
  * { margin: 0; padding: 0; box-sizing: border-box; }
  html, body {
    width: 1200px; height: 864px; overflow: hidden;
    background: var(--backdrop);
    font-family: "Source Sans 3", "Helvetica Neue", Arial, sans-serif;
  }
  .stage { position: relative; width: 1200px; height: 864px; }
  .card {
    position: absolute;
    width: 520px; height: 298px;
    background: var(--card);
    border: 1px solid var(--card-edge);
    box-shadow: 0 18px 40px rgba(0,0,0,0.45);
  }
  .card--back { left: 60px; top: 110px; }
  .card--front { left: 620px; top: 430px; }

  /* back */
  .back-brand {
    position: absolute; left: 0; right: 0; top: 100px;
    text-align: center;
    color: var(--silver);
    font-weight: 700; font-size: 34px; line-height: 1.05;
    letter-spacing: 1px;
  }
  .back-web {
    position: absolute; left: 0; right: 0; top: 214px;
    text-align: center;
    color: var(--muted);
    font-size: 12px; letter-spacing: 5px;
  }

  /* front */
  .front-brand {
    position: absolute; left: 34px; top: 112px; width: 220px;
    color: var(--accent);
    font-weight: 700; font-size: 30px; line-height: 1.05;
    display: flex; align-items: center; gap: 10px;
  }
  .front-brand .mark {
    flex: 0 0 14px; height: 14px; background: var(--accent);
  }
  .divider {
    position: absolute; left: 272px; top: 44px;
    width: 1px; height: 212px;
    background: linear-gradient(to bottom, transparent, var(--divider), transparent);
  }
  .contact { position: absolute; left: 290px; top: 62px; color: var(--ink); font-size: 14px; line-height: 1.3; }
  .contact .name { color: var(--accent); font-weight: 700; font-size: 18px; letter-spacing: 0.5px; }
  .contact .role { font-size: 13px; letter-spacing: 0.5px; margin-bottom: 6px; }
  .contact .address { margin-bottom: 4px; }
  .contact ul { list-style: none; }
  .contact li { display: flex; align-items: center; gap: 8px; height: 19px; }
  .contact svg { width: 12px; height: 12px; fill: var(--accent); flex: 0 0 12px; }
</style>
</head>
<body>
<main class="stage">
  <section class="card card--back" aria-label="Card back">
    <div class="back-brand">Kestrel Row<br>Builders, Inc.</div>
    <div class="back-web">www.kestrelrow.com</div>
  </section>

  <section class="card card--front" aria-label="Card front">
    <div class="front-brand"><span class="mark"></span><span>Kestrel Row Builders, Inc.</span></div>
    <div class="divider"></div>
    <div class="contact">
      <div class="name">EVAN MARLOW</div>
      <div class="role">PRESIDENT</div>
      <div class="address">4120 Harbor View Road<br>Bayside, NY 11360</div>
      <ul>
        <li><svg viewBox="0 0 12 12"><path d="M2.5 1 L4.5 1 L5.2 3.6 L4 4.6 Q5 6.9 7.4 8 L8.4 6.8 L11 7.5 L11 9.5 Q10.5 11 9 11 Q1 10 1 3 Q1 1.5 2.5 1Z"/></svg>555 0142 7781</li>
        <li><svg viewBox="0 0 12 12"><path d="M3 0.5h6a1 1 0 0 1 1 1v9a1 1 0 0 1-1 1H3a1 1 0 0 1-1-1v-9a1 1 0 0 1 1-1Zm0.8 1.5v7h4.4V2Z"/></svg>555 0187 3306</li>
        <li><svg viewBox="0 0 12 12"><path d="M3 1h5v3H3Zm-2 3.5h10v5H9v2H3v-2H1Zm3 4v2h4v-2Z"/></svg>555 0163 9924</li>
        <li><svg viewBox="0 0 12 12"><path d="M1 2.5h10v7H1Zm1 1v0.4L6 6.5l4-2.6v-0.4Z"/></svg>evan@kestrelrow.com</li>
        <li><svg viewBox="0 0 12 12"><circle cx="6" cy="6" r="5"/></svg>www.kestrelrow.com</li>
      </ul>
    </div>
  </section>
</main>
</body>
</html>
```